Professional Speaker needs a Business Card Design

I am a Professional Speaker and I need a design for my business cards. I would like for it to look sleek and professional but not too busy or cluttered. The colors I need are a bright blue, middle level gray and white. I also want a picture on both the front and back of the card. I have somewhat of a design that I created but it's something very basic. I was having an issue with submitting my images to Kelbrook Press because they weren't able to get me the exact colors I wanted. I would like to stick with something similar to what I came up with but am open to viewing your ideas.
Industry/Entity Type
Business
Contact Information for Business Card
Please refer to word document attached. It should be file 5 and that contains all of the details I need on my card. Also please be sure and use my Logo that is attached. The file is named logo front.

```html
<!DOCTYPE html>
<html lang="en">
<head>
<meta charset="utf-8">
<title>Marcus Fielding – Business Card</title>
<link rel="stylesheet" href="https://fonts.googleapis.com/css2?family=Cinzel:wght@400;600&family=Open+Sans:wght@400;600&family=Dancing+Script:wght@500&display=swap">
<style>
  :root{
    --bg:#e9e7e3;
    --black:#0c0d10;
    --grey:#3b3d42;
    --white:#f7f7f7;
    --blue:#3a5fd6;
    --bright:#2ab0e4;
    --band:rgba(58,80,200,.72);
    --text-dark:#222326;
    --text-light:#e8e8ea;
  }
  *{margin:0;padding:0;box-sizing:border-box}
  html,body{width:1200px;height:1023px;overflow:hidden;background:var(--bg)}
  .canvas{position:relative;width:1200px;height:1023px}
  .card{position:absolute;left:200px;width:800px;height:457px;overflow:hidden;
        background:var(--black);box-shadow:0 6px 18px rgba(0,0,0,.25)}
  .card--front{top:36px}
  .card--back{top:530px}

  /* front */
  .front__photo{position:absolute;left:470px;top:0;width:330px;height:330px;
        background:linear-gradient(160deg,#3a3b3f 0%,#c9cbd0 45%,#e6e7ea 75%,#9a9ca2 100%)}
  .brand{position:absolute;left:34px;top:76px;width:420px;display:flex;align-items:center;gap:16px}
  .brand__mark{flex:0 0 56px;width:56px;height:56px;border-radius:50%;background:var(--blue)}
  .brand__text{min-width:0}
  .brand__name{font-family:'Cinzel',serif;font-weight:600;font-size:31px;color:var(--blue);
        letter-spacing:.5px;line-height:1;white-space:nowrap}
  .brand__tagline{font-family:'Open Sans',sans-serif;font-weight:600;font-size:15px;color:var(--bright);
        letter-spacing:1px;margin-top:10px;white-space:nowrap}
  .front__band{position:absolute;left:0;top:200px;width:470px;height:130px;background:var(--white);
        padding:18px 34px;color:var(--text-dark)}
  .front__title{font-family:'Cinzel',serif;font-size:26px;letter-spacing:1px;white-space:nowrap}
  .front__line{font-family:'Open Sans',sans-serif;font-size:16px;margin-top:6px;color:#3a3a3e}
  .front__contact{font-family:'Open Sans',sans-serif;font-size:13px;margin-top:4px;color:#55565a;white-space:nowrap}
  .front__social{position:absolute;left:0;top:330px;width:800px;height:127px;background:var(--grey);
        display:grid;grid-template-columns:300px 300px;grid-auto-rows:34px;padding:22px 34px;column-gap:40px}
  .social{display:flex;align-items:center;gap:10px;font-family:'Open Sans',sans-serif;font-size:16px;color:var(--text-light)}
  .social__dot{width:22px;height:22px;border-radius:3px;background:#8fa6c9}

  /* back */
  .back__photo{position:absolute;left:0;top:250px;width:800px;height:207px;
        background:linear-gradient(180deg,#18191c 0%,#6b6c70 45%,#d5d6da 100%)}
  .back__motto{position:absolute;right:60px;top:70px;font-family:'Dancing Script',cursive;font-weight:500;
        font-size:72px;color:var(--bright);letter-spacing:2px;white-space:nowrap}
  .back__band{position:absolute;left:40px;top:0;width:64px;height:457px;background:var(--band);
        display:flex;align-items:center;justify-content:center}
  .back__roles{transform:rotate(90deg);white-space:nowrap;font-family:'Open Sans',sans-serif;font-weight:600;
        font-size:22px;letter-spacing:1px;color:var(--white)}
</style>
</head>
<body>
<div class="canvas">
  <section class="card card--front">
    <div class="front__photo" role="img" aria-label="Portrait photo of the speaker in a light checked shirt"></div>
    <div class="brand">
      <div class="brand__mark"></div>
      <div class="brand__text">
        <div class="brand__name">Marcus Fielding</div>
        <div class="brand__tagline">CLEARPATH MINDSET</div>
      </div>
    </div>
    <div class="front__band">
      <div class="front__title">CEO Fielding Unlimited</div>
      <div class="front__line">www.MarcusFieldingNow.com</div>
      <div class="front__contact">555-204-1836 | info@marcusfieldingnow.com</div>
    </div>
    <div class="front__social">
      <div class="social"><span class="social__dot"></span>Marcus Fielding</div>
      <div class="social"><span class="social__dot"></span>MarcusField85</div>
      <div class="social"><span class="social__dot"></span>M.Fielding85</div>
      <div class="social"><span class="social__dot"></span>Marcus Fielding</div>
    </div>
  </section>

  <section class="card card--back">
    <div class="back__photo" role="img" aria-label="Photo of the speaker smiling and holding a microphone"></div>
    <div class="back__motto">Love. Live. Life</div>
    <div class="back__band"><span class="back__roles">SPEAKER-AUTHOR-COACH</span></div>
  </section>
</div>
</body>
</html>
```